Premium Personal Brand — Facebook Banner (Used Across All Platforms)

Update — Additional Color Direction
In addition to the dark charcoal/slate direction already described, I'm also interested in seeing variants with:
Dark navy blue — Deep, authoritative, intelligence-community feel. Same textured/matte treatment, not flat or bright.
Warm charcoal with steel blue accent — Keep the dark base but introduce a subtle steel blue gradient, accent line, or tonal shift. Sophisticated, modern, adds dimension without adding color noise.
Both should maintain the same premium, restrained, architectural feel described in the original brief. No bright blues, no corporate PowerPoint energy — think midnight, think depth, think weight.
Everything else in the brief remains the same.
I am building a premium personal brand as an executive advisor to founders ($5M+ revenue).
This contest is Facebook-banner–focused, but the design must represent a visual system that will be reused across:
- LinkedIn
- YouTube
I- nstagram
- X (Twitter)
- Website hero sections and other brand touchpoints
Think of the Facebook banner as the primary expression of the brand — not a one-off graphic.
This project is about discovering a high-end visual style and brand feel, not decoration.
What to design
Please submit one cohesive visual system, shown primarily as:
- Facebook banner (primary focus)
The same design language should clearly translate to all platforms listed above.
Designers are responsible for using the current recommended dimensions for each platform.
Quick clarification on background direction:
Backgrounds should have depth and texture, not flat color fields. Avoid pure white, light grey, or solid black backgrounds. Think matte, architectural materials — stone, graphite, concrete, steel — not blank canvases. Subtle tonal variation is encouraged. Obvious gradients or decorative patterns are not.
Text to use
Primary Headline:
- Your Business Is Too Valuable To Be Run On Hope.
Subheadline:
- You didn’t build a business to become its prisoner.
Name:
Paul Whitaker
The headline should be the dominant visual element.
Logo note (important)
My personal logo is currently being finalized.
For this contest:
- Use a simple “PW” monogram placeholder
- Clean, bold, geometric sans-serif
- Do not design a logo
- The winning design must allow an easy logo swap later.
Headshot note (important)
- Please do not include a headshot in the banner design.
- Most platforms display a circular profile image separately.
- The banner should stand on its own using typography, layout, and tone only.
- Design the banner assuming the profile photo will sit nearby, not inside the banner.
Style direction
The design should feel:
- Premium
- Calm
- Confident
- Restrained
- High-trust
- Dark, neutral backgrounds are preferred.
- Fewer elements are better than more.
Think:
- Owner-level advisor
- Private equity / boardroom tone
- Industrial, Modern, Minimalist, Elite, Architectural, not decorative
What to avoid
Please do not submit designs that feel:
- Promotional, hype-driven, or salesy
- Like a coach, guru, or agency
- Bright, colorful, or gradient-heavy
- Busy or over-designed
- Based on stock photos
- No motivational speaker energy.
Reaction test
- If someone sees this banner on Facebook (or later on LinkedIn, YouTube, etc.), the reaction should be:
“That person is serious. I’d trust them with important decisions.”
Final note
- I am not looking for many variations.
- I am looking for one strong visual direction you believe in.
Simple beats clever.
- Restraint beats decoration.

```html
<!DOCTYPE html>
<html lang="en">
<head>
<meta charset="utf-8">
<title>Paul Whitaker — Banner</title>
<link rel="stylesheet" href="https://fonts.googleapis.com/css2?family=Inter+Tight:wght@300;400;500;700;800&display=swap">
<style>
  :root {
    --page-bg: #ffffff;
    --banner-base: #16282f;
    --banner-deep: #121f26;
    --banner-glow: rgba(70, 98, 92, 0.55);
    --banner-steel: rgba(62, 88, 116, 0.55);
    --monogram-tint: rgba(120, 150, 160, 0.08);
    --ribbon-tone: rgba(90, 118, 130, 0.16);
    --text-main: #eef1f1;
    --text-soft: #c9d2d4;
    --accent-sage: #9db5a4;
    --accent-steel: #8aa4bf;
    --pill-sage: #5f7a6b;
    --pill-steel: #4f6a86;
    --pill-ink: #f1f4f3;
  }
  * { box-sizing: border-box; margin: 0; padding: 0; }
  html, body {
    width: 1200px;
    height: 1163px;
    overflow: hidden;
    background: var(--page-bg);
    font-family: "Inter Tight", "Helvetica Neue", Arial, sans-serif;
  }
  .banner {
    position: absolute;
    left: 50px;
    top: 380px;
    width: 1100px;
    height: 404px;
    overflow: hidden;
    background:
      radial-gradient(ellipse 420px 160px at 47% 0%, var(--banner-glow) 0%, rgba(70,98,92,0) 100%),
      radial-gradient(ellipse 380px 220px at 100% 100%, var(--banner-steel) 0%, rgba(62,88,116,0) 100%),
      linear-gradient(180deg, var(--banner-base) 0%, var(--banner-deep) 100%);
  }
  .monogram-watermark {
    position: absolute;
    left: 50%;
    top: 40px;
    transform: translateX(-50%);
    font-weight: 800;
    font-size: 380px;
    line-height: 1;
    letter-spacing: -10px;
    color: var(--monogram-tint);
    white-space: nowrap;
  }
  .ribbon-art {
    position: absolute;
    border-radius: 50%;
    filter: blur(10px);
  }
  .ribbon-left {
    left: 95px; top: 10px; width: 175px; height: 230px;
    background: radial-gradient(ellipse at 50% 50%, var(--ribbon-tone) 0%, rgba(22,40,47,0) 72%);
  }
  .ribbon-right {
    left: 760px; top: 30px; width: 290px; height: 350px;
    background: radial-gradient(ellipse at 50% 50%, var(--ribbon-tone) 0%, rgba(22,40,47,0) 72%);
  }
  .spark { position: absolute; border-radius: 50%; }
  .spark-top { left: 808px; top: -12px; width: 46px; height: 32px; background: var(--pill-sage); border-radius: 0 0 50% 50%; }
  .spark-low { left: 345px; top: 297px; width: 28px; height: 28px; background: var(--pill-steel); }
  .copy {
    position: absolute;
    inset: 0;
    text-align: center;
    color: var(--text-main);
  }
  .brand-name {
    position: absolute;
    left: 0; right: 0;
    top: 85px;
    font-weight: 400;
    font-size: 28px;
    letter-spacing: 11px;
    text-indent: 11px;
    color: var(--text-soft);
  }
  .headline {
    position: absolute;
    left: 0; right: 0;
    top: 124px;
    font-weight: 500;
    font-size: 50px;
    line-height: 54px;
    letter-spacing: -1.8px;
  }
  .headline-line { display: block; white-space: nowrap; }
  .pill {
    display: inline-block;
    font-weight: 700;
    font-size: 34px;
    line-height: 1;
    letter-spacing: -1px;
    padding: 8px 22px 10px;
    border-radius: 30px;
    vertical-align: 6px;
    color: var(--pill-ink);
  }
  .pill-sage { background: var(--pill-sage); transform: rotate(2deg); margin-right: 6px; }
  .pill-steel { background: var(--pill-steel); transform: rotate(-3deg); margin-left: 6px; }
  .subhead {
    position: absolute;
    left: 0; right: 0;
    top: 249px;
    font-weight: 300;
    font-size: 29px;
    line-height: 32px;
    letter-spacing: -0.8px;
    color: var(--text-soft);
  }
  .hl-steel { color: var(--accent-steel); font-weight: 400; }
  .hl-sage { color: var(--accent-sage); font-weight: 400; }
</style>
</head>
<body>
  <section class="banner">
    <div class="monogram-watermark" aria-hidden="true">PW</div>
    <div class="ribbon-art ribbon-left" role="img" aria-label="Soft glass ribbon artwork"></div>
    <div class="ribbon-art ribbon-right" role="img" aria-label="Soft glass ribbon artwork"></div>
    <div class="spark spark-top" role="img" aria-label="Asterisk accent"></div>
    <div class="spark spark-low" role="img" aria-label="Asterisk accent"></div>

    <div class="copy">
      <p class="brand-name">PAUL WHITAKER</p>
      <h1 class="headline">
        <span class="headline-line">Your Business Is Too</span>
        <span class="headline-line"><span class="pill pill-sage">Valuable</span> To Be Run On <span class="pill pill-steel">Hope</span></span>
      </h1>
      <p class="subhead">You didn’t <span class="hl-steel">build a business</span> to<br>become its <span class="hl-sage">prisoner.</span></p>
    </div>
  </section>
</body>
</html>
```